Business card design needed

I run a Beautician studio (for 7 years now)
I offer
- Velmo Skin Glide
- Lumora Renew
- Nails
- Facials
- Manicure
- Foot Treatment
It might not be necessary to list all those treatments?
Maybe the link to the Website is sufficient?
I leave that up to you ...
(more info on www.BrowsAndBloomByMirela.com.au)
Velmo SkinGlide is our biggest success, It replaces waxing.
I would like to incorporate the logo into the Business Card.
We had many complaints regarding our old Business Cards as the Phone Number was to small.
On the backside, we would like a "your next Appointment" section.
Looking forward to you Design, cheers ... Mirela
Brows by Bloom by Mirela
14 Korrin Pde 3954 Berwick
www.BrowsAndBloomByMirela.com.au
03 8142 6639

```html
<!DOCTYPE html>
<html lang="en">
<head>
<meta charset="utf-8">
<title>Brows by Bloom by Mirela – Business Card</title>
<link rel="stylesheet" href="https://fonts.googleapis.com/css2?family=Cabin:wght@400;600;700&display=swap">
<style>
  :root {
    --page-bg: #d9d9d9;
    --card-bg: #ffffff;
    --accent-red: #d9401c;
    --bullet-green: #2e8b3a;
    --band-green: #8cc43f;
    --ink: #1a1a1a;
    --ink-soft: #555555;
    --band-grey: #8a8a8a;
  }
  * { box-sizing: border-box; margin: 0; padding: 0; }
  html, body { width: 1200px; height: 949px; overflow: hidden; }
  body {
    background: var(--page-bg);
    font-family: "Cabin", "Gill Sans", sans-serif;
    position: relative;
  }
  .card {
    position: absolute;
    left: 260px;
    width: 680px;
    height: 389px;
    background: var(--card-bg);
    box-shadow: 0 6px 18px rgba(0,0,0,0.25);
    overflow: hidden;
  }
  .card--front { top: 50px; }
  .card--back  { top: 510px; }

  /* Front */
  .services {
    position: absolute;
    left: 54px;
    top: 60px;
    list-style: none;
  }
  .services li {
    position: relative;
    padding-left: 24px;
    font-size: 18px;
    line-height: 23px;
    color: var(--accent-red);
  }
  .services li::before {
    content: "";
    position: absolute;
    left: 0;
    top: 7px;
    width: 9px;
    height: 9px;
    background: var(--bullet-green);
  }
  .brand {
    position: absolute;
    right: 58px;
    top: 120px;
    display: flex;
    align-items: center;
    gap: 10px;
  }
  .brand__mark {
    width: 22px;
    height: 22px;
    border-radius: 50%;
    background: var(--band-green);
  }
  .brand__name {
    font-size: 30px;
    font-weight: 600;
    color: var(--ink);
    letter-spacing: 1px;
  }
  .address {
    position: absolute;
    right: 58px;
    top: 178px;
    font-size: 17px;
    color: var(--ink);
  }
  .studio-name {
    position: absolute;
    left: 69px;
    top: 252px;
    font-size: 24px;
    font-weight: 700;
    color: var(--accent-red);
  }
  .phone {
    position: absolute;
    left: 69px;
    top: 286px;
    display: flex;
    align-items: center;
    gap: 12px;
    font-size: 24px;
    color: var(--ink);
  }
  .web-band {
    position: absolute;
    left: 0;
    bottom: 34px;
    width: 388px;
    height: 37px;
    background: var(--band-green);
    color: #ffffff;
    font-size: 15px;
    line-height: 37px;
    padding-left: 69px;
  }

  /* Back */
  .appointment {
    position: absolute;
    left: 58px;
    top: 92px;
    padding-left: 14px;
    border-left: 3px solid var(--ink-soft);
    font-size: 24px;
    color: var(--ink);
    line-height: 40px;
  }
  .back-band {
    position: absolute;
    left: 0;
    right: 0;
    bottom: 0;
    height: 56px;
    background: var(--band-grey);
  }
</style>
</head>
<body>
  <section class="card card--front" aria-label="Business card front">
    <ul class="services">
      <li>Velmo Skin Glide</li>
      <li>Lumora Renew</li>
      <li>Nails</li>
      <li>Facials</li>
      <li>Manicure</li>
      <li>Foot Treatment</li>
    </ul>

    <div class="brand">
      <span class="brand__mark"></span>
      <span class="brand__name">Velmo Skin Glide</span>
    </div>
    <p class="address">14 Korrin Pde 3954 Berwick</p>

    <p class="studio-name">Brows by Bloom by Mirela</p>
    <p class="phone">
      03 8142 6639
      <svg width="28" height="28" viewBox="0 0 28 28" aria-hidden="true">
        <circle cx="14" cy="14" r="12.5" fill="none" stroke="#1a1a1a" stroke-width="2"/>
        <path d="M10 7.5c-1.2.6-2 1.8-1.8 3.3.5 4 4.6 8.3 8.8 9.2 1.4.3 2.7-.4 3.4-1.6l-2.6-2.3-1.8 1c-1.8-.8-3.4-2.5-4.1-4.3l1.1-1.7L10 7.5z" fill="#1a1a1a"/>
      </svg>
    </p>

    <div class="web-band">www.BrowsAndBloomByMirela.com.au</div>
  </section>

  <section class="card card--back" aria-label="Business card back">
    <p class="appointment">Your Next Appointment:</p>
    <div class="back-band"></div>
  </section>
</body>
</html>
```